Beauty spa price list booklet. 16 pages from front to rear. Mainly white with compay logo

I need an A6 sized booklet for a beauty day spa.To incorporate our company logo, stock beauty photos (massages, facials, will send some examples over shortly.)16 Pages from front to rear.

Text sent over to be incorporated into the design as similar as the example one I've sent your as you can. Uploaded stock photos to be used in the correct places (Ie waxing photo on the waxing page etc....)

I've sent over a lot of the menu text but:

***I WILL WRITE UP AND SEND OVER THE REST OF THE LUMA SPA TREATMENT TEXT IN THE NEXT DAY OR TWO!!***

Target Market(s)

Customers using the spa. to take it away and keep at home.

Font styles to use
Serif
Sans Serif

Colors
00a990
33a6d7
ffffff

Requirements
Must have
• Company logo. Price lists.
• We like the use of white (for the most part. And teal tones in places.)
• Clear professional text with a good layout.

```html
<!DOCTYPE html>
<html lang="en">
<head>
<meta charset="utf-8">
<title>Luma House Day Spa – Treatment Menu</title>
<link rel="stylesheet" href="https://fonts.googleapis.com/css2?family=Quicksand:wght@400;500&display=swap">
<style>
  :root {
    --brand-blue: #1f6390;
    --title-blue: #1a6f99;
    --accent-sky: #4aa8d0;
    --ribbon-blue: rgba(63, 156, 196, 0.45);
    --ribbon-teal: rgba(143, 214, 208, 0.35);
    --ink: #1b1b1b;
    --paper-top: #ffffff;
    --paper-bottom: #a8d9ef;
  }
  * { margin: 0; padding: 0; box-sizing: border-box; }
  html, body { width: 1200px; height: 846px; overflow: hidden; }
  body { font-family: "Quicksand", sans-serif; color: var(--ink); }

  .spread {
    position: relative;
    width: 1200px;
    height: 846px;
    display: flex;
    background: linear-gradient(180deg, var(--paper-top) 0%, var(--paper-top) 30%, #e4f4fb 60%, var(--paper-bottom) 100%);
  }
  .page { position: relative; width: 600px; height: 846px; }

  .brand-mark { position: absolute; text-align: center; line-height: 1; }
  .brand-mark .dot { display: block; margin: 0 auto; border-radius: 50%; background: var(--brand-blue); }
  .brand-mark .name { display: block; color: var(--brand-blue); font-weight: 400; letter-spacing: 0.06em; }
  .brand-mark .sub { display: block; color: var(--ink); font-weight: 500; letter-spacing: 0.1em; }

  .cover .brand-mark { left: 150px; width: 300px; top: 40px; }
  .cover .brand-mark .dot { width: 44px; height: 44px; margin-bottom: 36px; }
  .cover .brand-mark .name { font-size: 40px; }
  .cover .brand-mark .sub { font-size: 21px; margin-top: 10px; }

  .ribbon-area {
    position: absolute; left: 0; top: 70px; width: 582px; height: 220px;
    border-radius: 0 0 60% 0 / 0 0 100% 0;
    background: linear-gradient(170deg, transparent 35%, var(--ribbon-teal) 60%, var(--ribbon-blue) 80%, transparent 100%);
  }

  .photo-set { position: absolute; left: 0; top: 0; }

  .cover-title { position: absolute; left: 190px; width: 400px; top: 718px; text-align: center; }
  .cover-title h1 { font-weight: 400; font-size: 44px; color: var(--title-blue); line-height: 1; }
  .cover-title p { font-size: 25px; margin-top: 8px; }

  .inside .brand-mark { left: 203px; width: 200px; top: 20px; }
  .inside .brand-mark .dot { width: 36px; height: 36px; margin-bottom: 47px; }
  .inside .brand-mark .name { font-size: 28px; }
  .inside .brand-mark .sub { font-size: 16px; margin-top: 7px; }

  .welcome {
    position: absolute; left: 65px; top: 205px; width: 482px;
    font-size: 19px; line-height: 26.6px; text-align: justify;
  }

  .price-section { position: absolute; left: 23px; top: 478px; }
  .price-section h2 { font-weight: 400; font-size: 28px; color: var(--accent-sky); }
  .price-list { list-style: none; margin-top: 30px; width: 307px; }
  .price-list li { display: flex; justify-content: space-between; font-size: 20px; line-height: 26.6px; }

  .waxing-photo { position: absolute; left: 352px; top: 533px; width: 236px; height: 187px;
    background: linear-gradient(135deg, #f4f1ee 0%, #e4bf9e 45%, #c98d62 70%, #f5f1ed 100%); }
</style>
</head>
<body>
<main class="spread">
  <section class="page cover">
    <div class="ribbon-area" role="img" aria-label="Decorative flowing teal ribbon"></div>

    <div class="brand-mark">
      <span class="dot"></span>
      <span class="name">luma house</span>
      <span class="sub">Day Spa</span>
    </div>

    <svg class="photo-set" width="600" height="846" viewBox="0 0 600 846">
      <defs>
        <linearGradient id="facialTone" x1="0" y1="0" x2="1" y2="1">
          <stop offset="0" stop-color="#f3ece8"/><stop offset="0.6" stop-color="#e2b9a4"/><stop offset="1" stop-color="#f4efec"/>
        </linearGradient>
        <linearGradient id="browTone" x1="0" y1="0" x2="1" y2="1">
          <stop offset="0" stop-color="#2a2a2a"/><stop offset="0.45" stop-color="#c99c86"/><stop offset="1" stop-color="#efd5c8"/>
        </linearGradient>
        <linearGradient id="massageTone" x1="0" y1="0" x2="1" y2="1">
          <stop offset="0" stop-color="#f1ebe4"/><stop offset="0.5" stop-color="#e7c2a8"/><stop offset="1" stop-color="#f5f3f0"/>
        </linearGradient>
      </defs>
      <polygon points="106,216 208,216 232,314 147,368 68,310" fill="url(#facialTone)" role="img" aria-label="Photo of a facial waxing treatment"/>
      <polygon points="40,356 290,438 285,698 32,770 0,730 0,400" fill="url(#browTone)" role="img" aria-label="Photo of a brow shaping treatment"/>
      <polygon points="306,400 474,328 593,466 498,623 320,583" fill="url(#massageTone)" role="img" aria-label="Photo of a relaxing back massage"/>
    </svg>

    <div class="cover-title">
      <h1>luma house spa</h1>
      <p>Our Treatment Menu</p>
    </div>
  </section>

  <section class="page inside">
    <div class="brand-mark">
      <span class="dot"></span>
      <span class="name">luma house</span>
      <span class="sub">Day Spa</span>
    </div>

    <p class="welcome">Welcome to Luma House Day Spa. We are situated in the heart of the beautiful seaside town of Seabrook in Eastmere. Conveniently placed for access to nearby bars and restaurants, the beach is only a short walk away. Luma House Day Spa invites you to relax and unwind in our peaceful setting, let us pamper you and restore your feelings of calm and wellness.</p>

    <div class="price-section">
      <h2>Waxing</h2>
      <ul class="price-list">
        <li><span>Eyebrow</span><span>£12.00</span></li>
        <li><span>Lip and Chin</span><span>£7.00</span></li>
        <li><span>Full Face</span><span>£12.00</span></li>
        <li><span>Under Arm</span><span>£10.00</span></li>
        <li><span>Half Leg</span><span>£16.00</span></li>
        <li><span>Three Quarter Leg</span><span>£20.00</span></li>
        <li><span>Full Leg</span><span>£23.00</span></li>
      </ul>
    </div>

    <div class="waxing-photo" role="img" aria-label="Photo of a leg waxing treatment"></div>
  </section>
</main>
</body>
</html>
```